Bingo Night

Willowmere Terraces is an Assisted Living Facility. We have 34 residents currently living in our facility. We provide care for elderly patients that need a slightly higher level of care than what can be provided at home. We are sending out this invitation to people in the surrounding community for Bingo night March 19, 2014 @ 6:00pm. The colors we would like to use are gold & maroon. Our address is 2497 W 38th St Tulsa, OK 74107. 918-526-3104. Also, the phrase "open to the public" should be incorporated on both sides.
Updates

Target Market(s)

Men and women between the ages of 50-90 years old.

Industry/Entity Type

Community

Font styles to use
Serif
Script

Requirements
Must have
• At least 4 pictures provided, our address, time of event, and phone number.

```html
<!DOCTYPE html>
<html lang="en">
<head>
<meta charset="utf-8">
<title>Willowmere Terraces – Bingo Night</title>
<link rel="stylesheet" href="https://fonts.googleapis.com/css2?family=Alfa+Slab+One&family=Pinyon+Script&family=Tinos&family=Marcellus&display=swap">
<style>
  :root {
    --maroon-deep: #3e0a0e;
    --maroon: #5e1218;
    --band: #975a60;
    --gold: #e3c86e;
    --gold-light: #f5e6a8;
    --gold-dark: #6b4a1c;
    --ink: #1a1208;
  }
  html, body { margin: 0; padding: 0; overflow: hidden; background: var(--maroon-deep); }
  .flyer { display: block; width: 1200px; height: 930px; }
  .venue-name { font-family: "Marcellus", "Times New Roman", serif; font-size: 46px; fill: var(--gold); }
  .event-word { font-family: "Alfa Slab One", "Georgia", serif; font-size: 86px; }
  .event-script { font-family: "Pinyon Script", cursive; font-size: 200px; }
  .ball-number { font-family: "Tinos", "Times New Roman", serif; fill: var(--ink); text-anchor: middle; dominant-baseline: central; }
  .public-note { font-family: "Tinos", "Times New Roman", serif; fill: var(--gold-light); text-anchor: middle; dominant-baseline: central; letter-spacing: 3px; }
  .public-note-top { font-size: 38px; }
  .public-note-middle { font-size: 52px; }
  .event-date { font-family: "Tinos", "Times New Roman", serif; font-size: 38px; fill: var(--gold); }
  .event-address { font-family: "Tinos", "Times New Roman", serif; font-size: 24px; fill: var(--gold); }
</style>
</head>
<body>
<svg class="flyer" viewBox="0 0 1200 930" xmlns="http://www.w3.org/2000/svg">
  <defs>
    <linearGradient id="bg" x1="0" y1="0" x2="1" y2="1">
      <stop offset="0" stop-color="#6a141b"/>
      <stop offset="1" stop-color="#3a080c"/>
    </linearGradient>
    <linearGradient id="title-gold" x1="0" y1="0" x2="1" y2="0">
      <stop offset="0" stop-color="#e9d079"/>
      <stop offset="0.55" stop-color="#c9a24e"/>
      <stop offset="1" stop-color="#5a2a1a"/>
    </linearGradient>
    <linearGradient id="script-gold" x1="0" y1="0" x2="1" y2="1">
      <stop offset="0" stop-color="#e6c86c"/>
      <stop offset="0.6" stop-color="#7a4a24"/>
      <stop offset="1" stop-color="#4a1a14"/>
    </linearGradient>
    <radialGradient id="ball" cx="0.4" cy="0.3" r="0.75">
      <stop offset="0" stop-color="#fff6d2"/>
      <stop offset="0.35" stop-color="#d9bd6a"/>
      <stop offset="0.75" stop-color="#7a5c22"/>
      <stop offset="1" stop-color="#1e1408"/>
    </radialGradient>
    <linearGradient id="photo-room" x1="0" y1="0" x2="0" y2="1">
      <stop offset="0" stop-color="#c9b79a"/><stop offset="1" stop-color="#5f6f5a"/>
    </linearGradient>
    <linearGradient id="photo-dog" x1="0" y1="0" x2="1" y2="1">
      <stop offset="0" stop-color="#d9a870"/><stop offset="1" stop-color="#5a4a52"/>
    </linearGradient>
    <linearGradient id="photo-visit" x1="0" y1="0" x2="1" y2="1">
      <stop offset="0" stop-color="#bfb6a8"/><stop offset="1" stop-color="#5e5a56"/>
    </linearGradient>
    <linearGradient id="photo-lobby" x1="0" y1="0" x2="0" y2="1">
      <stop offset="0" stop-color="#e0a060"/><stop offset="1" stop-color="#4a4050"/>
    </linearGradient>
    <filter id="shadow" x="-20%" y="-20%" width="140%" height="140%">
      <feDropShadow dx="2" dy="4" stdDeviation="3" flood-color="#000" flood-opacity="0.5"/>
    </filter>
  </defs>

  <rect class="background" width="1200" height="930" fill="url(#bg)"/>

  <rect class="band band-top" x="736" y="5" width="464" height="135" fill="var(--band)"/>
  <text class="public-note public-note-top" x="968" y="72">OPEN TO THE PUBLIC</text>

  <rect class="band band-middle" x="0" y="476" width="830" height="174" fill="var(--band)"/>
  <text class="public-note public-note-middle" x="400" y="565">OPEN TO THE PUBLIC</text>

  <text class="venue-name" x="68" y="138" textLength="635" lengthAdjust="spacingAndGlyphs">Willowmere Terraces</text>
  <text class="event-word" x="52" y="244" textLength="678" lengthAdjust="spacingAndGlyphs" fill="url(#title-gold)" filter="url(#shadow)">BINGO</text>
  <text class="event-script" x="165" y="390" textLength="550" lengthAdjust="spacingAndGlyphs" fill="url(#script-gold)" filter="url(#shadow)">Night</text>

  <g class="bingo-balls" filter="url(#shadow)">
    <circle cx="855" cy="388" r="52" fill="url(#ball)"/>
    <text class="ball-number" x="855" y="392" font-size="46" transform="rotate(-10 855 392)">6</text>
    <circle cx="600" cy="446" r="42" fill="url(#ball)"/>
    <text class="ball-number" x="600" y="450" font-size="38">8</text>
    <circle cx="95" cy="717" r="93" fill="url(#ball)"/>
    <text class="ball-number" x="90" y="717" font-size="66" transform="rotate(-12 90 717)">20</text>
    <circle cx="264" cy="683" r="40" fill="url(#ball)"/>
    <text class="ball-number" x="264" y="680" font-size="26" transform="rotate(20 264 680)">10</text>
    <circle cx="757" cy="735" r="65" fill="url(#ball)"/>
    <text class="ball-number" x="752" y="743" font-size="52" transform="rotate(30 752 743)">11</text>
  </g>

  <g class="photo-column">
    <rect x="848" y="167" width="322" height="178" fill="url(#photo-room)" role="img" aria-label="Photo: residents playing bingo at tables in the dining room"/>
    <rect x="925" y="362" width="245" height="173" fill="url(#photo-dog)" role="img" aria-label="Photo: a resident and visitor petting a golden therapy dog"/>
    <rect x="925" y="553" width="243" height="157" fill="url(#photo-visit)" role="img" aria-label="Photo: a visitor holding a small dog for a resident"/>
    <rect x="925" y="727" width="243" height="173" fill="url(#photo-lobby)" role="img" aria-label="Photo: the facility lobby with a flower arrangement on a glass table"/>
  </g>

  <text class="event-date" x="205" y="838" textLength="498" lengthAdjust="spacingAndGlyphs">March 19, 2014 @ 6:00pm</text>
  <text class="event-address" x="113" y="884" textLength="675" lengthAdjust="spacing">2497 W 38th St Tulsa, OK 74107.  Tel. 918-526-3104</text>
</svg>
</body>
</html>
```